Poster

I need a poster for my business, www.coastaltablejourneysbay.example which some information about the most important activities (Sangria Tasting, Iberian Ham, Charcuteries & Sherry Wine Tasting, Sailboat Experiences and Picnic Experiences). A3 Format. Social media included (@coastaltablejourneyctj), contact information included.

```html
<!DOCTYPE html>
<html lang="en">
<head>
<meta charset="utf-8">
<title>Coastal Table Journeys Poster</title>
<link href="https://fonts.googleapis.com/css2?family=Poppins:wght@400;500;600;700&family=Allura&display=swap" rel="stylesheet">
<style>
  :root {
    --stage: #a3a3a3;
    --ink: #000000;
    --gold: #f2a31b;
    --ring: #b8820f;
    --white: #ffffff;
    --cream: #fdf6dc;
    --dark-text: #1c1c1c;
  }
  * { margin: 0; padding: 0; box-sizing: border-box; }
  html, body { width: 1200px; height: 1200px; overflow: hidden; }
  body { background: var(--stage); font-family: "Poppins", sans-serif; position: relative; }

  .poster {
    position: absolute; left: 217px; top: 58px; width: 766px; height: 1083px;
    background: var(--ink); overflow: hidden; color: var(--white);
  }
  .hero-photo {
    position: absolute; left: 0; top: 0; width: 100%; height: 520px;
    background:
      linear-gradient(to bottom, rgba(0,0,0,0) 40%, rgba(0,0,0,0.8) 80%, #000 100%),
      radial-gradient(ellipse at 70% 45%, #8a6a3a 0%, #4a3a3a 35%, #2a2230 65%, #1a1620 100%);
  }
  .title { position: absolute; left: 0; width: 100%; text-align: center; }
  .title-script {
    top: 40px; font-family: "Allura", cursive; font-size: 92px; line-height: 1; z-index: 2;
  }
  .title-rule { position: absolute; top: 77px; height: 1px; background: rgba(255,255,255,0.8); }
  .title-rule.left { left: 149px; width: 140px; }
  .title-rule.right { left: 489px; width: 130px; }
  .title-main {
    font-weight: 700; font-size: 70px; line-height: 1; color: var(--gold);
    text-shadow: 0 2px 6px rgba(0,0,0,0.5);
  }
  .title-main.line1 { top: 110px; left: 8px; }
  .title-main.line2 { top: 172px; left: -12px; }
  .title-sub { top: 230px; font-size: 39px; font-weight: 400; line-height: 1.2; left: 12px; }
  .title-sub strong { font-weight: 600; }

  .activity { position: absolute; left: 0; width: 100%; }
  .activity-photo {
    position: absolute; left: 71px; width: 129px; height: 129px; border-radius: 50%;
    border: 9px solid var(--ring); box-shadow: inset 0 0 0 3px var(--white);
  }
  .activity-body { position: absolute; left: 222px; width: 492px; }
  .activity-title {
    color: var(--gold); font-weight: 700; font-size: 21px; line-height: 1.22; margin-bottom: 5px;
  }
  .activity-text { font-size: 13px; line-height: 1.18; }
  .activity-text + .activity-text { margin-top: 15px; }
  .activity-text.medium { font-weight: 500; }

  .photo-sangria { background: radial-gradient(circle at 40% 40%, #d9b49a, #6a4a40 60%, #2e2a2a); }
  .photo-ham { background: linear-gradient(160deg, #6f7e86, #3a3a36 50%, #2a1f1a); }
  .photo-sail { background: linear-gradient(to bottom, #c9cdd3 0%, #e7d6b8 45%, #3b5a78 60%, #1e3550 100%); }
  .photo-picnic { background: radial-gradient(circle at 50% 55%, #a35a30, #d9cfc4 55%, #6b8aa6); }

  .footer-edge { position: absolute; left: 0; top: 910px; width: 766px; height: 40px; }
  .footer {
    position: absolute; left: 0; top: 935px; width: 100%; height: 148px;
    background: linear-gradient(to bottom, var(--cream), #fffdf5);
    color: var(--dark-text);
  }
  .brand {
    position: absolute; left: 40px; top: 20px; display: flex; align-items: center; gap: 10px;
  }
  .brand-mark { width: 14px; height: 14px; background: var(--gold); }
  .brand-name {
    font-size: 15px; font-weight: 600; line-height: 1.1; color: var(--dark-text); width: 90px;
  }
  .call { position: absolute; left: 208px; top: 28px; }
  .call-label { color: var(--gold); font-weight: 700; font-size: 16px; line-height: 1.2; }
  .call-number { font-size: 17px; font-weight: 500; margin-top: 2px; }
  .contacts { position: absolute; left: 378px; top: 22px; font-size: 15.5px; line-height: 1.55; }
  .contact-row { display: flex; align-items: center; gap: 7px; }
  .contact-row svg { width: 15px; height: 15px; flex: none; }
</style>
</head>
<body>
<main class="poster">
  <div class="hero-photo" role="img" aria-label="Night view of hillside coastal apartments with warm lights"></div>

  <span class="title-rule left"></span>
  <span class="title-rule right"></span>
  <h1 class="title title-main line1">MARBELLA &amp;</h1>
  <div class="title title-main line2">ESTEPONA</div>
  <div class="title title-script">Enjoy</div>
  <div class="title title-sub">with <strong>Coastal Table Journeys</strong></div>

  <section class="activity" style="top:327px">
    <div class="activity-photo photo-sangria" style="top:0" role="img" aria-label="Friends enjoying glasses of sangria"></div>
    <div class="activity-body" style="top:0">
      <h2 class="activity-title">SANGRIA TASTING</h2>
      <p class="activity-text">During this experience, you will try four distinct types of authentic Sangria, each crafted with different wines and fresh, locally sourced ingredients.</p>
      <p class="activity-text">As you sip, immerse yourself in the vibrant atmosphere of Estepona, enjoying the flavors of marinated olives and local cheese included with your booking.</p>
    </div>
  </section>

  <section class="activity" style="top:465px">
    <div class="activity-photo photo-ham" style="top:0" role="img" aria-label="Olives and tapas on a table"></div>
    <div class="activity-body" style="top:7px">
      <h2 class="activity-title">IBERIAN HAM, CHARCUTERIES &amp;<br>SHERRY WINE TASTING</h2>
      <p class="activity-text">Indulge in the rich flavors of Spain with our Iberian Charcuteries &amp; Sherry Wine Tasting. Sample two premium Iberian hams, three distinct sausages, and a variety of olives, all perfectly paired with a selection of Sherry wines.</p>
    </div>
  </section>

  <section class="activity" style="top:604px">
    <div class="activity-photo photo-sail" style="top:0" role="img" aria-label="Sailboat on the sea at sunset"></div>
    <div class="activity-body" style="top:14px">
      <h2 class="activity-title">SAILBOAT EXPERIENCES</h2>
      <p class="activity-text medium">The Sailboat Sangria Tasting Experience is a unique and enchanting journey where you can relax and unwind while sailing along the beautiful coast of Estepona. Sip on exquisite artisanal sangria and enjoy gourmet appetizers in a serene</p>
    </div>
  </section>

  <section class="activity" style="top:743px">
    <div class="activity-photo photo-picnic" style="top:0" role="img" aria-label="Picnic basket with pastries by the sea"></div>
    <div class="activity-body" style="top:16px">
      <h2 class="activity-title">PICNIC EXPERIENCES</h2>
      <p class="activity-text medium">Indulge in a unique morning retreat with our Picnic Brunch Experience from Estepona to Playa Romana. Select from our gourmet picnic basket filled with freshly baked pastries, artisanal cheeses, cured meats, seasonal fruits, and decadent desserts.</p>
    </div>
  </section>

  <svg class="footer-edge" viewBox="0 0 766 40" preserveAspectRatio="none" aria-hidden="true">
    <polygon fill="#fdf6dc" points="0,20 20,18 40,22 60,14 85,19 110,12 130,17 150,10 170,16 190,13 215,20 240,11 265,15 290,9 310,16 335,12 360,18 385,10 410,15 430,19 455,12 480,16 505,11 530,18 555,14 580,20 605,13 630,17 655,12 680,19 705,14 730,18 750,13 766,16 766,40 0,40"/>
  </svg>

  <footer class="footer">
    <div class="brand">
      <span class="brand-mark"></span>
      <span class="brand-name">COASTAL TABLE JOURNEYS</span>
    </div>
    <div class="call">
      <div class="call-label">CALL US NOW</div>
      <div class="call-number">0034 600 123 456</div>
    </div>
    <div class="contacts">
      <div class="contact-row">
        <svg viewBox="0 0 16 16"><rect x="1" y="3" width="14" height="10" fill="#f2a31b"/><polyline points="1,3 8,9 15,3" fill="none" stroke="#fff" stroke-width="1.3"/></svg>
        <span>info@coastaltablejourneysbay.example</span>
      </div>
      <div class="contact-row">
        <svg viewBox="0 0 16 16" fill="none" stroke="#f2a31b" stroke-width="1.3"><circle cx="8" cy="8" r="6.5"/><ellipse cx="8" cy="8" rx="3" ry="6.5"/><line x1="1.5" y1="8" x2="14.5" y2="8"/></svg>
        <span>www.coastaltablejourneysbay.example</span>
      </div>
      <div class="contact-row">
        <svg viewBox="0 0 16 16" fill="none" stroke="#f2a31b" stroke-width="1.3"><path d="M2 3h12v8H7l-3 3v-3H2z"/></svg>
        <span>@coastaltablejourneyctj</span>
      </div>
    </div>
  </footer>
</main>
</body>
</html>
```